One page double sided catalog for fisheries

Create a double sided product catalog for a fresh yellowfin tuna exporting company in the Maldives called The Brindlecove Traders llc.
We export fresh yellowfin tuna caught from the wild using sustainable fishing methods to countries all across the globe. Our UPS are no MOQ requirements and Door Step Delivery. We aim to eliminate the middlemen in the business and deliver our products to our customer doorsteps in quantities that they can afford which will help them save money while getting the best fresh fish.
Main colors of our company are gold and blue to highlight premium quality while relating to the oceans
The catalog has to have 4-5 main point;
*Who we are
*What we do
*Our products
*About the Maldivian fisheries

The file attached is a draft we have received, but got disapproved as it doesn't have the catchy look and premium design elements we want to associate with our company and products.

Note: All text elements will be provided by us.

Industry/Entity Type

Business

Font styles to use
Serif
Sans Serif

Colors
0455a3

```html
<!DOCTYPE html>
<html lang="en">
<head>
<meta charset="utf-8">
<title>Brindlecove Traders – Catalog</title>
<link href="https://fonts.googleapis.com/css2?family=Cormorant+Garamond:wght@400;500&family=Montserrat:ital,wght@0,500;0,700;1,800&family=Open+Sans:wght@400;600&display=swap" rel="stylesheet">
<style>
  :root{
    --backdrop:#e4e2df;
    --ocean-deep:#0b1a2e;
    --ocean-mid:#1b4f86;
    --ocean-light:#3d86b8;
    --night:#0a0d12;
    --gold:#c9a15a;
    --gold-light:#e8d3a0;
    --paper:#ffffff;
    --paper-grey:#efefef;
    --ink:#3a3a3a;
    --ink-soft:#6b6b6b;
    --white:#ffffff;
  }
  *{box-sizing:border-box;margin:0;padding:0}
  html,body{width:1200px;height:802px;overflow:hidden}
  body{background:var(--backdrop);position:relative;font-family:"Open Sans",Arial,sans-serif}

  .sheet{position:absolute;box-shadow:0 4px 14px rgba(0,0,0,.25);overflow:hidden}
  .sheet--front{left:62px;top:55px;width:491px;height:693px;background:var(--paper-grey)}
  .sheet--back{left:645px;top:53px;width:492px;height:692px;background:var(--paper)}

  .photo{position:absolute;left:0;width:100%}
  .photo--school{top:0;height:93px;background:linear-gradient(180deg,#5d7f9d 0%,#9bb3c6 45%,#3e5f7e 100%)}
  .gold-rule{position:absolute;left:0;width:100%;height:3px;background:linear-gradient(90deg,var(--gold),var(--gold-light),var(--gold))}
  .sheet--front .gold-rule--top{top:93px}
  .photo--reef{top:96px;height:325px;background:linear-gradient(180deg,#2a7bb0 0%,#1a5187 30%,#0f2d55 65%,#0b1a2e 100%)}

  .brand{position:absolute;right:16px;top:20px;display:flex;flex-direction:column;align-items:center;gap:6px}
  .brand__dot{width:30px;height:30px;border-radius:50%;background:var(--gold)}
  .brand__name{font-family:"Cormorant Garamond",serif;font-size:14px;color:var(--white);letter-spacing:.3px}

  .tagline{position:absolute;right:16px;top:104px;font-family:"Cormorant Garamond",serif;font-size:23px;color:var(--white);word-spacing:2px}

  .promise{position:absolute;left:20px;top:174px;font-family:"Montserrat",sans-serif;font-weight:500;font-size:25px;color:var(--white);letter-spacing:1px}
  .pillars{position:absolute;left:19px;top:222px;display:grid;grid-template-columns:112px 116px 113px 110px;column-gap:0;color:var(--white)}
  .pillar{padding-right:10px}
  .pillar__title{font-family:"Montserrat",sans-serif;font-weight:500;font-size:11px;letter-spacing:.4px;line-height:14px;min-height:28px}
  .pillar__text{font-size:6.6px;line-height:11.6px}
  .pillar__text--justify{text-align:justify}
  .pillar--delivery .pillar__title{min-height:28px}
  .pillar--delivery{margin-top:0}

  .mission{position:absolute;left:0;top:421px;width:100%;height:104px;background:linear-gradient(90deg,#050608,#1a1d22 50%,#050608);color:var(--white);text-align:center;padding-top:12px;font-size:12.5px;line-height:17px}
  .mission__accent{font-family:"Montserrat",sans-serif;font-weight:800;font-style:italic;font-size:15px;letter-spacing:.5px}
  .mission__bold{font-family:"Montserrat",sans-serif;font-weight:700;font-size:14.5px}
  .sheet--front .gold-rule--mid{top:525px}

  .products{position:absolute;left:0;top:528px;width:100%;display:grid;grid-template-columns:repeat(3,1fr);padding:0 16px;text-align:center}
  .product__art{height:60px;margin:12px auto 8px;border-radius:4px}
  .product__art--loin{width:90px;background:linear-gradient(135deg,#f2a07e,#e98862)}
  .product__art--whole{width:135px;background:linear-gradient(90deg,#556373,#a9b2bb,#d9dde0)}
  .product__art--reef{width:70px;background:linear-gradient(135deg,#d8476a,#e8a24a)}
  .product__name{font-size:7.8px;color:var(--ink);letter-spacing:.2px}
  .product__note{font-size:5.8px;color:var(--ink-soft);line-height:8px;margin-top:2px}
  .product__pack{display:flex;align-items:center;justify-content:center;gap:4px;font-size:5.8px;color:var(--ink-soft);margin-top:2px}
  .product__pack::before{content:"";width:8px;height:8px;border-radius:50%;background:#333}

  .footer{position:absolute;left:20px;right:20px;top:670px;border-top:1px solid #b9b9b9;padding-top:4px;text-align:center;font-size:7.5px;color:var(--ink-soft)}

  .back-brand{position:absolute;left:0;width:100%;top:405px;display:flex;flex-direction:column;align-items:center;gap:8px}
  .back-brand__dot{width:70px;height:70px;border-radius:50%;background:var(--gold)}
  .back-brand__name{font-family:"Cormorant Garamond",serif;font-size:17px;color:#e7e7e7;letter-spacing:.4px}
  .sheet--back .gold-rule--bottom{top:532px}
  .photo--shoal{top:535px;height:157px;background:linear-gradient(180deg,#3a5968 0%,#24404f 55%,#152a36 100%)}
  .contact{position:absolute;right:20px;top:573px;text-align:right;color:var(--white);font-size:11px;line-height:13px}
  .contact__title{font-size:18px;line-height:24px;margin-bottom:1px}
</style>
</head>
<body>

<section class="sheet sheet--front">
  <div class="photo photo--school" role="img" aria-label="School of silver fish swimming near the surface"></div>
  <div class="gold-rule gold-rule--top"></div>
  <div class="photo photo--reef" role="img" aria-label="Underwater view of yellowfin tuna in deep blue sea"></div>

  <div class="brand">
    <span class="brand__dot"></span>
    <span class="brand__name">Brindlecove Traders</span>
  </div>

  <p class="tagline">seafood | sourcing | solutions</p>

  <h1 class="promise">OUR PROMISE</h1>

  <div class="pillars">
    <article class="pillar">
      <h2 class="pillar__title">FRESHNESS</h2>
      <p class="pillar__text pillar__text--justify">Our fishermen deliver freshly caught fish, on a daily basis, that are kept in temperature controlled cabinets which are then transferred to our EU Certified packing factories. Our fish are processed on the same day and delivered overnight to our customers all across the globe, meaning they get “A” grade fresh yellowfin tuna less than 24 hours from their processed time. It doesn't get any fresher than this.</p>
    </article>
    <article class="pillar">
      <h2 class="pillar__title">QUALITY</h2>
      <p class="pillar__text">Our fish is processed and packed in an ISO and EU certified factory where stringent quality control practices are maintained. The factory is regularly audited for health, safety and quality features.</p>
    </article>
    <article class="pillar">
      <h2 class="pillar__title">FLEXIBLE MOQ</h2>
      <p class="pillar__text">One of the greatest advantages of working with us is that we have absolutely no MOQ requirements for our customers. We serve according to our customer needs enabling them to have fresh stock throughout the year in volumes that they can afford to manage.</p>
    </article>
    <article class="pillar pillar--delivery">
      <h2 class="pillar__title">DOOR-STEP<br>DELIVERY</h2>
      <p class="pillar__text">We believe that, no matter where we are located, our customers deserve the best products and the best service, which is why we promise door step delivery to all our customers who require them. We partner with the best local courier agents to ensure our customer orders are delivered on a timely manner to their door steps, because we value your business and we believe every second counts.</p>
    </article>
  </div>

  <div class="mission">
    <p>formed to</p>
    <p class="mission__accent">REVOLUTIONIZE</p>
    <p>the <span class="mission__bold">FRESH TUNA</span></p>
    <p>exports from Maldives</p>
    <p>The Brindlecove</p>
  </div>
  <div class="gold-rule gold-rule--mid"></div>

  <div class="products">
    <figure class="product">
      <div class="product__art product__art--loin" role="img" aria-label="Raw yellowfin tuna loin"></div>
      <figcaption>
        <p class="product__name">YELLOW FIN TUNA LOINS</p>
        <p class="product__note">LOINS &amp; CHUNKS ARE VACUUMED PACKED,<br>STORED IN STYROFOAM BOXES WITH GEL ICE</p>
        <p class="product__pack">6KG, 15KG &amp; 25KG</p>
      </figcaption>
    </figure>
    <figure class="product">
      <div class="product__art product__art--whole" role="img" aria-label="Whole yellowfin tuna illustration"></div>
      <figcaption>
        <p class="product__name">YELLOW FIN TUNA H&amp;G/G&amp;G</p>
        <p class="product__note">HEADLESS GILL &amp; GUTTED, PACKED IN<br>CARDBOARD BOXES GROSS WEIGHT 90-95KG</p>
        <p class="product__pack">TWO PER BOX</p>
      </figcaption>
    </figure>
    <figure class="product">
      <div class="product__art product__art--reef" role="img" aria-label="Colourful reef fish"></div>
      <figcaption>
        <p class="product__name">REEF FISH</p>
        <p class="product__note">CUSTOMIZED ORDER FOR SPECIFIC<br>SPECIES OF REEF FISH CUSTOM</p>
      </figcaption>
    </figure>
  </div>

  <p class="footer">The Brindlecove Traders L.L.C | Seafood.Sourcing.Solutions | brindlecove.com.mv 771200 | 3324500</p>
</section>

<section class="sheet sheet--back">
  <div class="back-brand">
    <span class="back-brand__dot"></span>
    <span class="back-brand__name">BRINDLECOVE TRADERS</span>
  </div>
  <div class="gold-rule gold-rule--bottom"></div>
  <div class="photo photo--shoal" role="img" aria-label="Shoal of fish in dark teal water"></div>
  <address class="contact" style="font-style:normal">
    <p class="contact__title">Contact Us</p>
    <p>The Brindlecove Traders L.L.C</p>
    <p>Seafood.Sourcing.Solutions</p>
    <p>brindlecove.com.mv 771200</p>
    <p>3324500</p>
  </address>
</section>

</body>
</html>
```